Artisan Bread Company needs a business card

I need a business card design, for an artisan bread company called "Hollin's Bread".

I would like the logo on one side, and on the other, I would like it to say

Tavish Hollin
Baker
519.362.4175
hollinsbread@mailvexo.com

Not necessarily in that order- but it must have these.

Industry/Entity Type

Business

Font styles to use
Serif

Requirements
Must have
• The provided logo on the front, this on the back-
• Tavish Hollin
• Baker
• 519.362.4175
• hollinsbread@mailvexo.com

```html
<!DOCTYPE html>
<html lang="en">
<head>
<meta charset="utf-8">
<title>Hollin's Bread – Business Card</title>
<link rel="stylesheet" href="https://fonts.googleapis.com/css2?family=Noto+Serif&family=Arimo&display=swap">
<style>
  :root {
    --page: #e9e6e1;
    --card: #ffffff;
    --accent: #d63a26;
    --accent-dark: #b8281a;
    --ink: #111111;
    --fade-a: #f1ebe2;
    --fade-b: #e6d9c6;
    --fade-c: #ede3d4;
  }
  html, body {
    margin: 0;
    width: 1200px;
    height: 892px;
    overflow: hidden;
    background: var(--page);
  }
  .canvas {
    position: relative;
    width: 1200px;
    height: 892px;
  }
  .card {
    position: absolute;
    left: 250px;
    width: 700px;
    height: 400px;
    background: var(--card);
    box-shadow: 0 6px 18px rgba(0,0,0,0.18);
    overflow: hidden;
  }
  .card--front { top: 32px; }
  .card--back { top: 460px; }
  .card-art {
    position: absolute;
    left: 0;
    top: 0;
  }

  .holder-name {
    position: absolute;
    right: 70px;
    top: 182px;
    margin: 0;
    font-family: "Noto Serif", serif;
    font-weight: 400;
    font-size: 44px;
    line-height: 1.2;
    color: var(--accent);
    letter-spacing: 0.5px;
  }
  .holder-role {
    position: absolute;
    right: 40px;
    top: 236px;
    margin: 0;
    font-family: "Arimo", sans-serif;
    font-weight: 400;
    font-size: 30px;
    line-height: 1.2;
    color: var(--ink);
  }
  .contact-list {
    position: absolute;
    left: 60px;
    bottom: 34px;
    margin: 0;
    padding: 0;
    list-style: none;
    font-family: "Arimo", sans-serif;
    font-weight: 400;
    font-size: 24px;
    color: var(--ink);
  }
  .contact-item {
    display: flex;
    align-items: center;
    gap: 14px;
    height: 36px;
  }
  .contact-icon {
    display: block;
    width: 18px;
    height: 18px;
    flex: none;
  }
</style>
</head>
<body>
<div class="canvas">

  <section class="card card--front">
    <svg class="card-art" width="700" height="400" viewBox="0 0 700 400">
      <defs>
        <clipPath id="photo-band">
          <path d="M0 0H700V26C600 34 530 60 480 118C440 166 380 176 300 178C200 180 80 182 0 186Z"/>
        </clipPath>
        <linearGradient id="tile-burger" x1="0" y1="0" x2="1" y2="1">
          <stop offset="0" stop-color="#d9a15c"/><stop offset="1" stop-color="#6d8a3a"/>
        </linearGradient>
        <linearGradient id="tile-pink" x1="0" y1="0" x2="1" y2="1">
          <stop offset="0" stop-color="#e87fb0"/><stop offset="1" stop-color="#d45a93"/>
        </linearGradient>
        <linearGradient id="tile-choc" x1="0" y1="0" x2="1" y2="1">
          <stop offset="0" stop-color="#8a6048"/><stop offset="1" stop-color="#d9cfc4"/>
        </linearGradient>
        <linearGradient id="tile-fruit" x1="0" y1="0" x2="1" y2="1">
          <stop offset="0" stop-color="#3a2a24"/><stop offset="1" stop-color="#e5b93a"/>
        </linearGradient>
        <linearGradient id="tile-sandwich" x1="0" y1="0" x2="1" y2="1">
          <stop offset="0" stop-color="#c98a4a"/><stop offset="1" stop-color="#e46a3a"/>
        </linearGradient>
      </defs>

      <g clip-path="url(#photo-band)">
        <rect x="0" y="0" width="160" height="200" fill="url(#tile-burger)" role="img" aria-label="Photo of a sesame burger bun with fillings"/>
        <rect x="160" y="0" width="150" height="200" fill="url(#tile-pink)" role="img" aria-label="Photo of a pink piped celebration cake"/>
        <rect x="310" y="0" width="140" height="200" fill="url(#tile-choc)" role="img" aria-label="Photo of a birthday cake with chocolate lattice and strawberries"/>
        <rect x="450" y="0" width="130" height="200" fill="url(#tile-fruit)" role="img" aria-label="Photo of a fruit cake topped with cookies"/>
        <rect x="580" y="0" width="120" height="200" fill="url(#tile-sandwich)" role="img" aria-label="Photo of a filled bread roll sandwich"/>
      </g>

      <path class="wave-band" d="M700 26C600 34 530 60 480 118C440 166 380 176 300 178C200 180 80 182 0 186V198C80 194 200 192 300 190C388 188 452 176 494 126C540 72 610 44 700 38Z" fill="var(--accent)"/>
      <path class="wave-line" d="M0 204C80 200 200 198 300 196C392 194 458 182 500 132C544 80 612 52 700 46" fill="none" stroke="var(--accent-dark)" stroke-width="2"/>
    </svg>

    <h1 class="holder-name">Tavish Hollin</h1>
    <p class="holder-role">Baker</p>

    <ul class="contact-list">
      <li class="contact-item">
        <svg class="contact-icon" width="18" height="18" viewBox="0 0 18 18" aria-hidden="true">
          <rect width="18" height="18" fill="var(--accent)"/>
          <path d="M5 4h3l1 3-2 1c1 2 2 3 3 3l1-2 3 1v3c-6 1-10-4-9-9z" fill="#fff"/>
        </svg>
        <span>519.362.4175</span>
      </li>
      <li class="contact-item">
        <svg class="contact-icon" width="18" height="18" viewBox="0 0 18 18" aria-hidden="true">
          <rect width="18" height="18" fill="var(--accent)"/>
          <rect x="3.5" y="5" width="11" height="8" fill="#fff"/>
          <path d="M3.5 5l5.5 4.5L14.5 5" fill="none" stroke="var(--accent)" stroke-width="1.2"/>
        </svg>
        <span>hollinsbread@mailvexo.com</span>
      </li>
    </ul>
  </section>

  <section class="card card--back">
    <svg class="card-art" width="700" height="400" viewBox="0 0 700 400">
      <defs>
        <linearGradient id="fade-1" x1="0" y1="0" x2="0" y2="1">
          <stop offset="0" stop-color="var(--fade-a)"/><stop offset="1" stop-color="var(--fade-b)"/>
        </linearGradient>
        <linearGradient id="fade-2" x1="0" y1="0" x2="0" y2="1">
          <stop offset="0" stop-color="var(--fade-b)"/><stop offset="1" stop-color="var(--fade-c)"/>
        </linearGradient>
      </defs>
      <rect x="0" y="0" width="112" height="400" fill="url(#fade-1)" role="img" aria-label="Faded photo of a bread loaf with seeds"/>
      <rect x="116" y="0" width="112" height="400" fill="url(#fade-2)" role="img" aria-label="Faded photo of flour and grains"/>
      <rect x="232" y="0" width="112" height="400" fill="url(#fade-1)" role="img" aria-label="Faded photo of a seeded bread roll"/>
      <rect x="348" y="0" width="112" height="400" fill="url(#fade-2)" role="img" aria-label="Faded photo of a sandwich with fresh vegetables"/>
      <rect x="464" y="0" width="112" height="400" fill="url(#fade-1)" role="img" aria-label="Faded photo of a golden bun"/>
      <rect x="580" y="0" width="120" height="400" fill="url(#fade-2)" role="img" aria-label="Faded photo of a whisk in a mixing bowl"/>
    </svg>
  </section>

</div>
</body>
</html>
```